依頼詳細
■ 重視する点/検討基準

以下のポイントを重視して選択させて頂きます。

・新聞折込チラシでの問い合わせアップにつながる新しさと信頼感
・サービスの特徴がわかりやすい
・高齢者の方にも読みやすい
・高齢でスマートフォン操作に慣れていない方にも、HPにアクセスしやすい構成
記載項目
■ 入れて欲しい内容
・有効期限
・通常価格25,000円が今だけ税込5000円
・見積もり費用や出張費用、その他の追加料金がかからないこと
・お家一軒丸ごとが洗浄範囲であること
・会社情報とHPにつながるQRの記載欄、集計のためのチラシ識別番号欄があること

※会社情報やロゴはこちらで入れるので、どこに何を配置するかわかるようにアテで入れていただけますと幸いです。
サイズ
B4
ページ数
片面
希望イメージ
シンプル 複雑
単色 カラフル
暗い 明るい
日常 高級
遊び心 厳粛
未来的 伝統的
女性的 男性的
希望する色
納品ファイル
• イラストレーター形式 (.ai)
補足説明
確認用のPDFデータと、文字編集可能なイラストレータデータでの納品をお願いいたします。

チラシデータは今後ターゲットや内容を変えて配布する予定ですので、二次利用があります。
【追記 締め切りを延長いたしました】
排水管洗浄のイメージを変えたいです。
従来の排水管チラシやネットにあるような形ではなく、新しい+αのアイデアを採用いたします。

シニアの方がターゲットなので、読みやすく分かりやすいデザインを希望いたします。
■ 選んだ理由

排水管洗浄をイメージやすいイラスト、写真の使い方や、綺麗な文字の組み方が素敵でした。
施工後に水回りのトラブルが解決し、綺麗になるのがイメージしやすかったです。

■ 提案者全員のお礼・コメント

提出いただいた2パターンとも、今までになかった見せ方と信頼感がありました。
素敵なご提案をいただき、弊社の社員一同、大変喜んでおります。
ありがとうございました。

```html
<!DOCTYPE html>
<html lang="ja">
<head>
<meta charset="UTF-8">
<title>排水管洗浄サービス チラシ</title>
<link href="https://fonts.googleapis.com/css2?family=Noto+Sans+JP:wght@400;500;700;900&family=Roboto+Condensed:wght@700&display=swap" rel="stylesheet">
<style>
:root{
  --navy:#1b3a6b;
  --blue:#2a86d1;
  --sky:#dceffb;
  --pale:#eef7fd;
  --yellow:#ffe14a;
  --cream:#fff7c7;
  --orange:#f07a12;
  --red:#e23b2e;
  --ink:#23303f;
  --grey:#6b7785;
  --white:#ffffff;
}
*{margin:0;padding:0;box-sizing:border-box}
html,body{width:846px;height:1200px;overflow:hidden;background:var(--white)}
body{font-family:"Noto Sans JP",sans-serif;color:var(--ink);position:relative}
.abs{position:absolute}
.ph{position:absolute;border-radius:6px}

/* header */
.header{left:0;top:0;width:846px;height:215px;background:linear-gradient(180deg,var(--pale),var(--sky))}
.pipe-art{left:0;top:0;width:60px;height:90px;background:linear-gradient(90deg,#b9c7d6,#e6edf3);border-radius:0 0 30px 0}
.title{left:68px;top:14px;font-size:40px;font-weight:900;color:var(--navy);letter-spacing:1px;white-space:nowrap}
.title small{font-size:29px}
.tags{left:60px;top:78px;display:flex;align-items:center;gap:4px;font-weight:900;font-size:24px;color:var(--navy)}
.tag{background:var(--yellow);padding:2px 10px;border-radius:4px}
.tag-red{color:var(--red)}
.lead{left:60px;top:124px;font-size:29px;font-weight:900;color:var(--navy);white-space:nowrap}
.lead .pro{background:var(--navy);color:var(--white);padding:0 8px;border-radius:4px;margin-right:4px}
.hero-art{left:650px;top:84px;width:176px;height:122px;background:linear-gradient(135deg,#ffffff,#bcdcf2);border-radius:12px}

/* campaign */
.camp-band{left:20px;top:218px;width:806px;height:40px;background:var(--blue);color:var(--white);font-size:25px;font-weight:900;text-align:center;line-height:40px;border-radius:6px 6px 0 0}
.camp-box{left:20px;top:258px;width:806px;height:166px;border:3px solid var(--blue);border-top:none;background:var(--white)}
.staff-art{left:28px;top:266px;width:92px;height:148px;background:linear-gradient(180deg,#f4e3d3,#e8eef5);border-radius:8px}
.service{left:130px;top:268px;font-size:22px;font-weight:900;color:var(--navy)}
.service .maru{display:inline-block;width:30px;height:30px;border-radius:50%;background:var(--red);color:var(--white);text-align:center;line-height:30px;font-size:20px}
.service u{text-decoration:none;border-bottom:3px solid var(--yellow)}
.regular{left:258px;top:306px;font-size:16px;font-weight:700}
.regular .strike{font-size:18px}
.nanto{left:138px;top:318px;width:76px;height:76px;border-radius:50%;background:var(--red);color:var(--white);font-weight:900;font-size:17px;display:flex;align-items:center;justify-content:center;transform:rotate(-8deg)}
.price{left:220px;top:318px;font-family:"Roboto Condensed",sans-serif;font-weight:700;font-size:86px;line-height:1;color:var(--orange);letter-spacing:-2px}
.price-yen{left:412px;top:350px;font-size:38px;font-weight:900;color:var(--orange)}
.tax{left:424px;top:330px;font-size:13px;font-weight:700;color:var(--orange)}
.noextra{left:258px;top:400px;font-size:15px;font-weight:700;color:var(--navy);line-height:1.2}
.noextra b{border-bottom:2px solid var(--red)}
.limit{left:555px;top:272px;width:100px;height:100px;border-radius:50%;background:var(--yellow);color:var(--navy);text-align:center;font-weight:900;padding-top:18px}
.limit .l1{font-size:14px;background:var(--navy);color:var(--white);padding:1px 6px;border-radius:3px}
.limit .l2{font-size:22px;margin-top:6px}
.limit .l3{font-size:14px}
.first{left:672px;top:300px;width:140px;height:100px;border:2px solid var(--red);border-radius:8px;text-align:center;color:var(--ink);font-weight:700;font-size:12px;padding-top:8px}
.first .num{font-size:15px;color:var(--red);font-weight:900}
.first .num b{font-size:34px}

/* features */
.feat-band{left:20px;top:436px;width:806px;height:40px;background:var(--navy);color:var(--white);font-size:25px;font-weight:900;line-height:40px;padding-left:170px;border-radius:4px}
.feat-band em{font-style:normal;color:var(--yellow);font-size:30px}
.feat-art{left:725px;top:424px;width:96px;height:56px;background:linear-gradient(180deg,#f3e0cd,#d7e6f3);border-radius:8px 8px 0 0}
.point{left:20px;width:806px;background:var(--pale);border-radius:6px}
.point1{top:484px;height:150px}
.point2{top:642px;height:130px}
.badge{position:absolute;left:12px;top:10px;width:44px;height:52px;background:var(--blue);color:var(--white);text-align:center;font-weight:900;border-radius:6px;font-size:10px;padding-top:4px}
.badge b{display:block;font-size:24px;line-height:1.1}
.p-head{position:absolute;left:66px;top:8px;font-size:20px;font-weight:900;color:var(--navy);line-height:1.25}
.p-sub{position:absolute;left:16px;top:66px;font-size:21px;font-weight:900;color:var(--blue);white-space:nowrap}
.p-body{position:absolute;left:16px;font-size:11px;line-height:1.55;color:var(--ink)}
.time{position:absolute;display:flex;font-size:12px;font-weight:700}
.time span{padding:2px 8px;border:1px solid var(--blue);background:var(--white)}
.time span:first-child{background:var(--blue);color:var(--white)}
.photo{width:120px;height:100px;background:linear-gradient(135deg,#a9b6c0,#d9e2e8)}
.cap{position:absolute;font-size:12px;font-weight:700;color:var(--navy)}
.arrow{position:absolute;width:0;height:0;border-left:9px solid var(--blue);border-top:8px solid transparent;border-bottom:8px solid transparent}
.house-art{left:330px;top:650px;width:488px;height:116px;background:linear-gradient(180deg,#e9f4fb,#cfe5d7);border-radius:6px}
.noextra2{position:absolute;left:16px;top:96px;font-size:12px;font-weight:700;color:var(--red);border:1px solid var(--red);background:var(--white);padding:2px 8px}

/* apply */
.apply{left:0;top:782px;width:846px;height:330px;background:var(--cream)}
.apply-head{left:20px;top:792px;width:520px;height:40px;background:var(--blue);color:var(--white);font-size:20px;font-weight:900;line-height:40px;padding-left:16px;border-radius:4px}
.apply-period{left:550px;top:792px;width:276px;height:40px;background:var(--navy);color:var(--yellow);font-weight:900;font-size:16px;line-height:40px;text-align:center;border-radius:4px}
.apply-period b{font-size:22px}
.tel-box{left:20px;top:846px;width:330px;height:250px;background:var(--white);border:3px solid var(--navy);border-radius:8px}
.tel-title{position:absolute;left:0;top:0;width:100%;height:34px;background:var(--navy);color:var(--white);font-weight:900;font-size:17px;line-height:34px;text-align:center}
.tel-num{position:absolute;left:14px;top:52px;font-family:"Roboto Condensed",sans-serif;font-weight:700;font-size:44px;color:var(--navy);display:flex;align-items:center;gap:6px}
.tel-hours{position:absolute;left:16px;top:120px;font-size:12px;line-height:1.6;color:var(--ink)}
.tel-note{position:absolute;left:16px;top:176px;width:294px;font-size:14px;font-weight:700;background:var(--yellow);color:var(--navy);padding:8px;text-align:center;border-radius:4px}
.caller-art{left:365px;top:846px;width:150px;height:250px;background:linear-gradient(180deg,#f6e2cf,#fbe9b0);border-radius:8px}
.web-box{left:530px;top:846px;width:296px;height:250px;background:var(--white);border:3px solid var(--blue);border-radius:8px}
.web-title{position:absolute;left:0;top:0;width:100%;height:34px;background:var(--blue);color:var(--white);font-weight:900;font-size:17px;line-height:34px;text-align:center}
.qr-slot{position:absolute;left:24px;top:56px;width:130px;height:130px;border:2px dashed var(--grey);background:var(--pale)}
.always{position:absolute;left:170px;top:64px;width:100px;height:100px;border-radius:50%;background:var(--yellow);color:var(--navy);text-align:center;font-weight:900;font-size:14px;padding-top:22px;line-height:1.3}
.always b{font-size:20px}
.web-note{position:absolute;left:16px;top:198px;width:258px;font-size:12px;font-weight:700;color:var(--navy);text-align:center}

/* footer */
.footer{left:20px;top:1122px;width:806px;height:66px;display:flex;align-items:center;gap:26px}
.company small{display:block;font-size:11px}
.company{font-size:26px;font-weight:900;color:var(--navy);line-height:1.1}
.address{font-size:11px;line-height:1.6;color:var(--ink)}
.flyer-id{margin-left:auto;display:flex;border:1px solid var(--ink);font-size:12px;font-weight:700}
.flyer-id span{padding:6px 8px}
.flyer-id span:first-child{background:var(--ink);color:var(--white)}
.flyer-id span:last-child{font-size:16px;padding:4px 16px}
</style>
</head>
<body>

<header>
  <div class="abs header"></div>
  <div class="abs pipe-art" role="img" aria-label="排水管のイラスト"></div>
  <div class="abs hero-art" role="img" aria-label="きれいになった水回りのイラスト"></div>
  <h1 class="abs title">排水管のお掃除<small>は</small>お済み<small>ですか？</small></h1>
  <div class="abs tags">
    <span class="tag">汚れ</span>・<span class="tag">ニオイ</span>・<span class="tag">詰まり</span>を<span class="tag-red">解消！</span>
  </div>
  <p class="abs lead"><span class="pro">プロ</span>に任せて、暮らしをもっと快適に！</p>
</header>

<section>
  <div class="abs camp-band">地域一斉お掃除キャンペーン特別価格！</div>
  <div class="abs camp-box"></div>
  <div class="abs staff-art" role="img" aria-label="案内するスタッフのイラスト"></div>
  <p class="abs service">お家一軒<span class="maru">丸</span>ごと <u>排水管洗浄サービス</u></p>
  <p class="abs regular">通常価格 <span class="strike">25,000</span>円 のところ</p>
  <div class="abs nanto">なんと！</div>
  <p class="abs price">5,000</p>
  <p class="abs tax">（税込）</p>
  <p class="abs price-yen">円</p>
  <p class="abs noextra">もちろん、<b>追加料金は一切頂きません</b></p>
  <div class="abs limit">
    <span class="l1">期間限定</span>
    <div class="l2">00/00</div>
    <div class="l3">(●) まで</div>
  </div>
  <div class="abs first">
    戸建住宅にお住いの方<br>
    <span class="num">先着<b>30</b>名様</span><br>限定
  </div>
</section>

<section>
  <div class="abs feat-band">当社の排水管洗浄は<em>ココ</em>がちがいます！</div>
  <div class="abs feat-art" role="img" aria-label="説明するスタッフのイラスト"></div>

  <div class="abs point point1">
    <div class="badge">POINT<b>1</b></div>
    <p class="p-head">職人ワザ！<br>プロのお掃除技術</p>
    <p class="p-sub">水の力で汚れを徹底洗浄</p>
    <p class="p-body" style="top:98px;width:180px">専用の機材とノズルを汚水マスから入れて、高圧ジェット水流で管内をきれいに流します。</p>
    <div class="time" style="left:200px;top:100px;flex-direction:column;text-align:center"><span>作業時間</span><span>2時間程度</span></div>
    <div class="ph photo" style="left:300px;top:12px" role="img" aria-label="汚水マスを開ける作業の写真"></div>
    <div class="ph photo" style="left:470px;top:12px" role="img" aria-label="高圧洗浄の作業写真"></div>
    <div class="ph photo" style="left:640px;top:12px;width:150px" role="img" aria-label="点検と片付けの写真"></div>
    <div class="arrow" style="left:440px;top:56px"></div>
    <div class="arrow" style="left:610px;top:56px"></div>
    <span class="cap" style="left:300px;top:120px">①汚水マス開栓</span>
    <span class="cap" style="left:470px;top:120px">②高圧洗浄</span>
    <span class="cap" style="left:640px;top:120px">③点検・片付け</span>
  </div>

  <div class="abs point point2">
    <div class="badge">POINT<b>2</b></div>
    <p class="p-head">洗浄範囲は<br>“お家一軒丸ごと”</p>
    <p class="p-body" style="top:62px;width:290px">台所・浴室・洗面所・トイレの排水管から<br>屋外の汚水マスまで、まとめて洗浄します。</p>
    <p class="noextra2">作業範囲による追加料金は一切かかりません</p>
  </div>
  <div class="abs house-art" role="img" aria-label="家の排水管と洗浄範囲を示す図"></div>
</section>

<section>
  <div class="abs apply"></div>
  <div class="abs apply-head">お電話からもネットからもお申込みください！</div>
  <div class="abs apply-period">キャンペーン期間 <b>00月00日</b> まで</div>

  <div class="abs tel-box">
    <div class="tel-title">お電話からのお申込み</div>
    <div class="tel-num">
      <svg width="36" height="36" viewBox="0 0 24 24" aria-hidden="true"><path fill="#1b3a6b" d="M6.6 10.8a15.1 15.1 0 0 0 6.6 6.6l2.2-2.2a1 1 0 0 1 1-.25 11.4 11.4 0 0 0 3.6.57 1 1 0 0 1 1 1V20a1 1 0 0 1-1 1A17 17 0 0 1 3 4a1 1 0 0 1 1-1h3.5a1 1 0 0 1 1 1c0 1.25.2 2.450.57 3.57a1 1 0 0 1-.25 1z"/></svg>
      0120-000-000
    </div>
    <p class="tel-hours">受付時間 9:00〜18:00（年末年始を除く）<br>お気軽にお電話ください。</p>
    <p class="tel-note">「チラシを見た」とお伝えください</p>
  </div>

  <div class="abs caller-art" role="img" aria-label="電話で申し込む女性のイラスト"></div>

  <div class="abs web-box">
    <div class="web-title">ネット申込はこちら</div>
    <div class="qr-slot" role="img" aria-label="ホームページへのQRコード記載欄"></div>
    <div class="always"><b>24時間</b><br>365日<br>受付</div>
    <p class="web-note">スマートフォンのカメラで読み取ってください</p>
  </div>
</section>

<footer class="abs footer">
  <div class="company"><small>株式会社</small>●●●●●ホーム</div>
  <p class="address">〒000-0000<br>●●県●●市●●町0-0-0　TEL 00-0000-0000</p>
  <div class="flyer-id"><span>チラシ番号</span><span>8888</span></div>
</footer>

</body>
</html>
```